Stationery Design Project

We need letterhead and business cards designed for our consulting firm. Color scheme, mostly deep blue (see logo). We are a commercial consulting work out firm, nationwide (large loans, $10MM and up). Visit our website for more info.
Updates

Project Deadline Extended
Reason: Meeting tomorrow morning to make final final decision. Would like this project to stay open to be able to provide feed back and receive final edits and approve. Thank you!!!

Target Market(s)

High end investors

Industry/Entity Type

Business

Requirements
Must have
• Letterhead must have the logo and the address

4817 Larkmoor Avenue, Suite 210, San Diego, CA 92107
Nice to have
• It would be nice to incorporate a watermark of all or some portion of the logo on the letterhead, or at least for the 2nd sheets.

Maybe our phone number: 858.555.0174
and/or webiste: www.tollandridgecap.example
Should not have
• Target users and audience of this will be men so, frilly or whimsical type designs are not preferred.

```html
<!DOCTYPE html>
<html lang="en">
<head>
<meta charset="utf-8">
<title>Tolland Ridge Capital — Stationery</title>
<link href="https://fonts.googleapis.com/css2?family=Open+Sans:wght@400;600&display=swap" rel="stylesheet">
<style>
  :root {
    --backdrop: #97a0a5;
    --paper: #ffffff;
    --accent: #5bbdf3;
    --ink: #4d4f52;
    --brand: #46565f;
    --rule: #b9bec2;
    --holder: #2f8ed0;
  }
  * { box-sizing: border-box; margin: 0; padding: 0; }
  html, body { width: 1200px; height: 900px; overflow: hidden; }
  body {
    position: relative;
    background: var(--backdrop);
    font-family: "Open Sans", Arial, sans-serif;
    color: var(--ink);
  }
  .sheet { position: absolute; background: var(--paper); overflow: hidden; }
  .edge-band { position: absolute; left: 0; top: 0; bottom: 0; width: 12px; background: var(--accent); }

  .brand { position: absolute; display: flex; align-items: center; gap: 6px; white-space: nowrap; }
  .brand-mark { width: 9px; height: 9px; background: var(--accent); flex: none; }
  .brand-name { font-weight: 600; color: var(--brand); letter-spacing: 0.02em; }

  .contact { position: absolute; font-size: 6px; line-height: 9px; white-space: nowrap; }
  .contact .label, .contact .web { color: var(--accent); }

  /* Letterhead */
  .letterhead { left: 75px; top: 104px; width: 496px; height: 701px; }
  .letterhead .brand { left: 37px; top: 66px; }
  .letterhead .brand-name { font-size: 13px; }
  .letterhead .address { left: 270px; top: 74px; }
  .letterhead .phone-web { left: 384px; top: 74px; }

  /* Envelope */
  .envelope { left: 613px; top: 195px; width: 520px; height: 259px; }
  .envelope .brand { right: 36px; top: 46px; }
  .envelope .brand-name { font-size: 13px; }
  .envelope .address { right: 130px; top: 220px; text-align: right; }
  .envelope .phone-web { left: 402px; top: 220px; }

  /* Business cards */
  .card { border-radius: 11px; }
  .card-front { left: 651px; top: 527px; width: 212px; height: 130px; }
  .card-front .brand { left: 0; right: 0; top: 58px; justify-content: center; }
  .card-front .brand-name { font-size: 12px; }

  .card-back { left: 888px; top: 591px; width: 212px; height: 129px; }
  .card-back .brand { left: 12px; top: 30px; gap: 4px; }
  .card-back .brand-mark { width: 6px; height: 6px; }
  .card-back .brand-name { font-size: 6.5px; }
  .holder { position: absolute; left: 101px; top: 23px; white-space: nowrap; }
  .holder-name { font-size: 7.5px; font-weight: 600; color: var(--holder); line-height: 9px; }
  .holder-title { font-size: 6px; line-height: 9px; }
  .holder-rule { position: absolute; left: 101px; right: 0; top: 45px; height: 1px; background: var(--rule); }
  .card-back .address { left: 101px; top: 55px; }
  .card-back .lines { left: 101px; top: 78px; }
</style>
</head>
<body>

  <section class="sheet letterhead" aria-label="Letterhead">
    <div class="edge-band"></div>
    <div class="brand"><span class="brand-mark"></span><span class="brand-name">Tolland Ridge Capital</span></div>
    <p class="contact address">4817 Larkmoor Avenue, Suite 210<br>San Diego, CA 92107</p>
    <p class="contact phone-web"><span class="label">tel:</span> 858.555.0174<br><span class="web">www.tollandridgecap.example</span></p>
  </section>

  <section class="sheet envelope" aria-label="Envelope">
    <div class="edge-band"></div>
    <div class="brand"><span class="brand-mark"></span><span class="brand-name">Tolland Ridge Capital</span></div>
    <p class="contact address">4817 Larkmoor Avenue, Suite 210<br>San Diego, CA 92107</p>
    <p class="contact phone-web"><span class="label">tel:</span> 858.555.0174<br><span class="web">www.tollandridgecap.example</span></p>
  </section>

  <section class="sheet card card-front" aria-label="Business card front">
    <div class="brand"><span class="brand-mark"></span><span class="brand-name">Tolland Ridge Capital</span></div>
  </section>

  <section class="sheet card card-back" aria-label="Business card back">
    <div class="brand"><span class="brand-mark"></span><span class="brand-name">Tolland Ridge Capital</span></div>
    <div class="holder">
      <p class="holder-name">Daniel Mercer</p>
      <p class="holder-title">Chief Executive Officer</p>
    </div>
    <div class="holder-rule"></div>
    <p class="contact address">4817 Larkmoor Avenue, Suite 210<br>San Diego, CA 92107</p>
    <p class="contact lines">
      <span class="label">tel:</span> 858.555.0174<br>
      <span class="label">fax:</span> 858.555.0188<br>
      <span class="label">cell:</span> 858.555.0192<br>
      <span class="label">e-mail:</span> info@tollandridge.example<br>
      <span class="web">www.tollandridgecap.example</span>
    </p>
  </section>

</body>
</html>
```